Stationary for Vornik Consulting

Hi

I am after stationary designs for my company - Vornik Consulting. I have a logo - recently designed by PixelHarbor. Vornik ( sales spelt backwards ) is a sales consultancy - including sales training, sales coaching and business management.

I have attached some of the artwork I already have, as well as a few ideas
1. Use supplied logo's
2. back of business card to use the logo with the dark background and white text
3. details to be included on card are
Logo
Delmo Kastrani
p: +61409371826
e: delmo@vornikconsulting.com.au
w: www.vornikconsulting.com.au
PO Box 417, Larkmere North, Westvale, 3990

4. I am after designs for business cards, A4 letterhead and A5 letterhead

Thanks in Advance

Delmo

```html
<!DOCTYPE html>
<html lang="en">
<head>
<meta charset="utf-8">
<title>Vornik Consulting Stationery</title>
<link href="https://fonts.googleapis.com/css2?family=Arimo:wght@400;700&display=swap" rel="stylesheet">
<style>
  :root {
    --slate: #2f4650;
    --orange: #e0452a;
    --paper: #ffffff;
    --backdrop: #6d6d6d;
    --ink: #2a2f33;
  }
  * { margin: 0; padding: 0; box-sizing: border-box; }
  html, body { width: 1200px; height: 1000px; overflow: hidden; }
  body {
    position: relative;
    background: var(--backdrop);
    font-family: "Arimo", Arial, sans-serif;
    color: var(--ink);
  }
  .sheet { position: absolute; background: var(--paper); overflow: hidden; }
  .brand {
    position: absolute;
    font-family: "Arimo", Arial, sans-serif;
    font-weight: 700;
    color: var(--slate);
    white-space: nowrap;
    line-height: 1;
  }

  /* Business card front */
  .card-front { left: 115px; top: 34px; width: 308px; height: 190px; }
  .card-front .band-slate { position: absolute; left: 0; top: 0; width: 17px; height: 100%; background: var(--slate); }
  .card-front .band-orange { position: absolute; left: 17px; top: 0; width: 8px; height: 100%; background: var(--orange); }
  .card-front .brand { right: 23px; top: 37px; font-size: 14px; }
  .card-front .person { position: absolute; left: 40px; top: 80px; }
  .card-front .person-name { font-size: 13px; font-weight: 700; color: var(--slate); }
  .card-front .person-role { font-size: 6px; margin-top: 1px; }
  .card-front .contact { position: absolute; left: 40px; top: 116px; font-size: 7px; line-height: 14.8px; }

  /* Business card back and plain face */
  .card-back { left: 444px; top: 34px; width: 308px; height: 190px; background: var(--slate); }
  .card-back .brand { color: var(--paper); }
  .card-plain { left: 777px; top: 34px; width: 308px; height: 190px; }
  .card-back .brand, .card-plain .brand {
    left: 0; right: 0; top: 82px; text-align: center; font-size: 24px;
  }

  /* Letterhead */
  .letterhead { left: 52px; top: 264px; width: 491px; height: 693px; }
  .letterhead .brand { right: 28px; top: 40px; font-size: 17px; }
  .letterhead .footer {
    position: absolute; left: 0; bottom: 0; width: 100%; height: 29px;
    background: var(--slate);
    display: flex; align-items: center; justify-content: center;
    color: var(--paper); font-size: 6.5px;
  }
  .letterhead .footer::before, .letterhead .footer::after {
    content: ""; position: absolute; top: 0; width: 11px; height: 100%; background: var(--orange);
  }
  .letterhead .footer::before { left: 0; }
  .letterhead .footer::after { right: 0; }
  .footer-item { padding: 0 10px; }
  .footer-item + .footer-item { border-left: 1px solid rgba(255,255,255,0.7); }

  /* Envelope front */
  .envelope-front { left: 603px; top: 325px; width: 565px; height: 269px; }
  .envelope-front .brand { left: 39px; top: 45px; font-size: 15px; }
  .envelope-front .tab-slate { position: absolute; left: 0; top: 91px; width: 24px; height: 29px; background: var(--slate); }
  .envelope-front .tab-orange { position: absolute; left: 24px; top: 91px; width: 9px; height: 29px; background: var(--orange); }
  .envelope-front .return-address { position: absolute; left: 44px; top: 91px; font-size: 6px; line-height: 8.8px; color: #111; }

  /* Envelope back */
  .envelope-back { left: 603px; top: 629px; width: 560px; height: 268px; }
  .envelope-back .flap { position: absolute; left: 0; top: 0; }
  .envelope-back .brand { left: 0; right: 0; top: 24px; text-align: center; font-size: 26px; }
</style>
</head>
<body>

  <section class="sheet card-front">
    <div class="band-slate"></div>
    <div class="band-orange"></div>
    <div class="brand">Vornik Consulting</div>
    <div class="person">
      <div class="person-name">Delmo Kastrani</div>
      <div class="person-role">Owner / Founder</div>
    </div>
    <div class="contact">
      <div>M&nbsp; +61409371826</div>
      <div>E&nbsp; delmo@vornikconsulting.com.au</div>
      <div>W&nbsp; www.vornikconsulting.com.au</div>
      <div>PO Box 417, Larkmere North, Westvale, 3990</div>
    </div>
  </section>

  <section class="sheet card-back">
    <div class="brand">Vornik Consulting</div>
  </section>

  <section class="sheet card-plain">
    <div class="brand">Vornik Consulting</div>
  </section>

  <section class="sheet letterhead">
    <div class="brand">Vornik Consulting</div>
    <div class="footer">
      <span class="footer-item">e-mail: delmo@vornikconsulting.com.au</span>
      <span class="footer-item">web: www.vornikconsulting.com.au</span>
      <span class="footer-item">PO Box 417, Larkmere North, Westvale, 3990</span>
    </div>
  </section>

  <section class="sheet envelope-front">
    <div class="brand">Vornik Consulting</div>
    <div class="tab-slate"></div>
    <div class="tab-orange"></div>
    <div class="return-address">
      <div>e-mail: delmo@vornikconsulting.com.au</div>
      <div>web: www.vornikconsulting.com.au</div>
      <div>PO Box 417, Larkmere North, Westvale, 3990</div>
    </div>
  </section>

  <section class="sheet envelope-back">
    <svg class="flap" width="560" height="80" viewBox="0 0 560 80">
      <path d="M0 0 C6 40 20 74 48 74 L512 74 C540 74 554 40 560 0" fill="none" stroke="#888" stroke-width="0.8"/>
    </svg>
    <div class="brand">Vornik</div>
  </section>

</body>
</html>
```